Ice cream manufacturer need packaging design

We are a artisanal ice cream maker - Gelato makers - we are in the process of commercialising our products to restaurants, hotels. catering services and large supermarkets. It is a unique product which we are bringing to the market as it is a traditionally made ice cream using fresh ingredients rather than flavouring. We will be selling our products in small individual containers of 100ml as well as family boxes of 500ml and 1l. A little bit like Velmoret.We need the packaging to ooze quality, it needs to scream that' this is not your average industrial air full ice cream, but quality natural ingredients'The packaging needs to include:- The brand name Quilna as a nice logo- The flavour- Ingredients section.- Batch number- Expire date (should read see lid)- The name and address of the manufacturer - Pastry Lodge, Rue Kaddour Semlali, Draria, Alger, Algerie - Special storage conditions - To be stored at -18 degrees and left at room temperature for 10 min before consumption.- Net weight: 100ml or 500ml or 1l

Industry/Entity Type

Food Production

Colors

Designer to choose colors to be used in the design.

Requirements
Must have
• Brand Name and Flavour with some reference to ice cream.
Nice to have
• It must convey that this is a quality product.
Should not have
• It should not have a funny or playful message

```html
<!DOCTYPE html>
<html lang="en">
<head>
<meta charset="utf-8">
<title>Quilna Strawberry – Packaging</title>
<link rel="stylesheet" href="https://fonts.googleapis.com/css2?family=Lobster+Two:ital,wght@1,700&family=Arimo:wght@400&display=swap">
<style>
  :root {
    --backdrop: #a7a7a7;
    --night: #141414;
    --blush: #f0a9bd;
    --berry-red: #a3162a;
    --gold: #e9c25a;
    --gold-dark: #b8862c;
    --cream: #f6f0e6;
    --scoop: #f2d6d2;
    --berry: #c81c2a;
    --tagline-yellow: #f2df7a;
    --tagline-pink: #f3a8c0;
    --ink: #1c1c1c;
  }
  * { box-sizing: border-box; margin: 0; padding: 0; }
  html, body { width: 1200px; height: 849px; overflow: hidden; }
  body { background: var(--backdrop); position: relative; }

  .tub-label {
    position: absolute; left: 250px; top: 215px;
    width: 380px; height: 450px;
    background: var(--blush);
    overflow: hidden;
  }
  .lid {
    position: absolute; left: 660px; top: 245px;
    width: 390px; height: 390px; border-radius: 50%;
    background: var(--blush);
    padding: 16px;
  }
  .lid-face {
    position: relative; width: 100%; height: 100%;
    border-radius: 50%; overflow: hidden; background: var(--blush);
  }

  .dark-field { position: absolute; left: 0; top: 0; width: 100%; background: var(--night); }
  .tub-label .dark-field { height: 290px; }
  .lid-face .dark-field { height: 215px; }

  .brand-name {
    position: absolute; left: 0; width: 100%; text-align: center;
    font-family: "Lobster Two", cursive; font-style: italic; font-weight: 700;
    color: var(--cream);
  }
  .tub-label .brand-name { top: 60px; font-size: 56px; }
  .lid-face .brand-name { top: 30px; font-size: 48px; }

  .tagline {
    position: absolute; left: 0; width: 100%; text-align: center;
    font-family: "Lobster Two", cursive; font-style: italic; font-weight: 700;
  }
  .tub-label .tagline { top: 158px; font-size: 17px; color: var(--tagline-yellow); }
  .lid-face .tagline { top: 112px; font-size: 16px; color: var(--tagline-pink); }

  .gold-ribbon { position: absolute; left: 0; width: 100%; }
  .tub-label .gold-ribbon { top: 266px; height: 40px; }
  .lid-face .gold-ribbon { top: 192px; height: 40px; }

  .product-photo {
    position: absolute; border-radius: 60px;
    background: linear-gradient(90deg, var(--scoop) 0%, var(--scoop) 45%, var(--berry) 55%, var(--berry) 100%);
  }
  .tub-label .product-photo { left: 115px; top: 192px; width: 240px; height: 112px; }
  .lid-face .product-photo { left: 85px; top: 140px; width: 200px; height: 92px; border-radius: 46px; }

  .flavour {
    position: absolute; left: 0; width: 100%; text-align: center;
    font-family: "Lobster Two", cursive; font-style: italic; font-weight: 700;
    color: var(--berry-red);
  }
  .tub-label .flavour { top: 325px; font-size: 44px; }
  .lid-face .flavour { top: 240px; font-size: 40px; }

  .net-weight {
    position: absolute; left: 0; width: 100%; text-align: center;
    font-family: "Arimo", sans-serif; color: var(--ink);
  }
  .tub-label .net-weight { top: 392px; font-size: 16px; }
  .lid-face .net-weight { top: 298px; font-size: 14px; }
</style>
</head>
<body>

  <section class="tub-label">
    <div class="dark-field"></div>
    <div class="brand-name">Quilna</div>
    <div class="tagline">Glace Italienne de Qualité</div>
    <svg class="gold-ribbon" viewBox="0 0 380 40" preserveAspectRatio="none">
      <path d="M0 30 Q190 4 380 18 L380 24 Q190 12 0 36 Z" fill="var(--gold)"/>
      <path d="M0 36 Q190 12 380 24 L380 26 Q190 15 0 38 Z" fill="var(--gold-dark)"/>
    </svg>
    <div class="product-photo" role="img" aria-label="Photo of a scoop of strawberry ice cream beside a fresh strawberry"></div>
    <div class="flavour">Strawberry</div>
    <div class="net-weight">Net Wt. 100ml (3.3814 oz.)</div>
  </section>

  <section class="lid">
    <div class="lid-face">
      <div class="dark-field"></div>
      <div class="brand-name">Quilna</div>
      <div class="tagline">Glace Italienne de Qualité</div>
      <svg class="gold-ribbon" viewBox="0 0 358 40" preserveAspectRatio="none">
        <path d="M0 30 Q179 4 358 18 L358 24 Q179 12 0 36 Z" fill="var(--gold)"/>
        <path d="M0 36 Q179 12 358 24 L358 26 Q179 15 0 38 Z" fill="var(--gold-dark)"/>
      </svg>
      <div class="product-photo" role="img" aria-label="Photo of a scoop of strawberry ice cream beside a fresh strawberry"></div>
      <div class="flavour">Strawberry</div>
      <div class="net-weight">Net Wt. 100ml (3.3814 oz.)</div>
    </div>
  </section>

</body>
</html>
```